Bold and colurful E-liquid Design Template

I'm looking for a new label for my house range of vape e-liquids. I currently have almost 40 flavours, so I'm looking for a single label design that I can modify to create the rest of the flavours.
Each label will have the same design, but I'll change the color for each flavour and the name.
I'd like the label to be predominantly text based with bold text and bold colours. I like bold typographic styles. Also for each flavour I'd like to add 1 - 3 letters to represent the flavour. This can be in a larger font.
eg for
Blueberry I'll use the letter B
Pineapple Peach will use PP
Cinnamon Blueberry Muffin uses CBM
The colour used on the label will also be important so they stand out nicely on the shelf.
I've attached a psd mockup of the bottles I'll be using.

```html
<!DOCTYPE html>
<html lang="en">
<head>
<meta charset="utf-8">
<title>E-Liquid Label Range</title>
<link rel="stylesheet" href="https://fonts.googleapis.com/css2?family=Montserrat:wght@400;600;700&family=Playfair+Display:wght@800&display=swap">
<style>
  :root {
    --page: #d6d6d6;
    --label-bg: #111417;
    --ink: #ffffff;
    --blue: #5bc6d9;
    --blue-deep: #2a55c9;
    --yellow: #f5dc3a;
    --yellow-deep: #e8741e;
    --orange: #e2912f;
    --orange-deep: #e2601c;
  }
  * { box-sizing: border-box; margin: 0; padding: 0; }
  html, body { width: 1200px; height: 1061px; overflow: hidden; }
  body {
    background: var(--page);
    font-family: "Montserrat", sans-serif;
    color: var(--ink);
    display: flex;
    align-items: center;
    justify-content: center;
    gap: 22px;
  }
  .label {
    position: relative;
    width: 372px;
    height: 314px;
    background: var(--label-bg);
    overflow: hidden;
  }
  .label--blueberry { --accent: var(--blue); --accent-deep: var(--blue-deep); }
  .label--pineapple { --accent: var(--yellow); --accent-deep: var(--yellow-deep); }
  .label--cinnamon  { --accent: var(--orange); --accent-deep: var(--orange-deep); }

  .smoke {
    position: absolute;
    inset: 10px 0 0 0;
    background:
      radial-gradient(ellipse 30% 45% at 18% 30%, color-mix(in srgb, var(--accent) 45%, transparent), transparent 70%),
      radial-gradient(ellipse 35% 40% at 25% 80%, color-mix(in srgb, var(--accent-deep) 45%, transparent), transparent 70%),
      radial-gradient(ellipse 25% 35% at 50% 55%, color-mix(in srgb, var(--accent) 25%, transparent), transparent 70%),
      radial-gradient(ellipse 25% 30% at 70% 88%, color-mix(in srgb, var(--accent) 25%, transparent), transparent 70%);
  }
  .range-band {
    position: absolute;
    top: 0; left: 0; right: 0;
    height: 11px;
    background: var(--accent);
    color: var(--label-bg);
    font-weight: 700;
    font-size: 10px;
    line-height: 11px;
    padding-left: 32px;
    letter-spacing: 0.2px;
    word-spacing: 3px;
  }
  .flavour {
    position: absolute;
    top: 40px;
    left: 38px;
    width: 180px;
    height: 210px;
    writing-mode: vertical-rl;
    font-family: "Playfair Display", serif;
    font-weight: 800;
    font-size: 44px;
    line-height: 0.88;
    display: flex;
    justify-content: center;
    align-items: center;
    text-align: center;
  }
  .label--cinnamon .flavour { font-size: 27px; line-height: 1.05; }
  .info {
    position: absolute;
    top: 28px;
    left: 178px;
    width: 186px;
    font-size: 7.2px;
    line-height: 1.28;
  }
  .info h3 {
    color: var(--accent);
    font-size: 9px;
    font-weight: 700;
    margin-top: 6px;
  }
  .info h3:first-child { margin-top: 0; }
  .info .caps { text-transform: uppercase; }
  .icons {
    position: absolute;
    left: 248px;
    top: 244px;
    display: flex;
    gap: 16px;
    align-items: center;
  }
  .maker {
    position: absolute;
    left: 183px;
    top: 282px;
    font-size: 6px;
    font-weight: 700;
  }
  .origin {
    position: absolute;
    right: 22px;
    top: 290px;
    font-size: 6px;
    font-weight: 700;
    text-align: center;
    line-height: 1.2;
  }
  .spec {
    position: absolute;
    bottom: 8px;
    font-size: 14px;
    font-weight: 600;
  }
  .spec--volume { left: 30px; }
  .spec--strength { left: 118px; }
</style>
</head>
<body>

<article class="label label--blueberry">
  <div class="smoke" role="img" aria-label="Blue smoke wisps illustration"></div>
  <div class="range-band">PREMEMUM E-LIQUID</div>
  <h2 class="flavour">Blueberry</h2>
  <div class="info">
    <h3>INGREDIENTS:</h3>
    <p class="caps">Vegetable glycerin, propylene glycol<br>Natural &amp; artificial flavor 3%<br>Nicotine by volume</p>
    <p>May contain trace elements of nuts or seeds</p>
    <h3>WARNING:</h3>
    <p>This product contains nicotine, a chemical known to the State of California to cause birth defects or other reproductive harm. This product is for adult use only. Keep away from children and pets. Do not ingest or apply to the skin. If nicotine poisoning occurs seek immediate medical attention.</p>
    <h3>USE WITH CAUTION:</h3>
    <p>Lorem ipsum dolor sit amet, consectetur adipisicing elit, sed do eiusmod tempor incididunt ut labore et dolore magna aliqua. Ut enim ad minim veniam, quis nostrud exercitation ullamco</p>
  </div>
  <div class="icons">
    <svg width="18" height="18" viewBox="0 0 18 18"><circle cx="9" cy="9" r="7" fill="#fff"/></svg>
    <svg width="22" height="20" viewBox="0 0 22 20"><path d="M11 1 L21 19 H1 Z" fill="#fff" stroke="#fff" stroke-linejoin="round" stroke-width="2"/><rect x="10" y="7" width="2" height="6" fill="#111417"/><rect x="10" y="15" width="2" height="2" fill="#111417"/></svg>
    <svg width="18" height="20" viewBox="0 0 18 20" fill="none" stroke="#fff" stroke-width="1.5"><circle cx="10" cy="3" r="2"/><path d="M10 6 L8 12 L5 19 M8 12 L11 19 M9 8 L14 11"/><rect x="1" y="14" width="4" height="5"/></svg>
  </div>
  <div class="maker">MANUFACTURED BY:</div>
  <div class="origin">MADE IN<br>NEW ZEALAND</div>
  <div class="spec spec--volume">60ML</div>
  <div class="spec spec--strength">6MG</div>
</article>

<article class="label label--pineapple">
  <div class="smoke" role="img" aria-label="Yellow and orange smoke wisps illustration"></div>
  <div class="range-band">PREMEMUM E-LIQUID</div>
  <h2 class="flavour">Pineapple<br>Peach</h2>
  <div class="info">
    <h3>INGREDIENTS:</h3>
    <p class="caps">Vegetable glycerin, propylene glycol<br>Natural &amp; artificial flavor 3%<br>Nicotine by volume</p>
    <p>May contain trace elements of nuts or seeds</p>
    <h3>WARNING:</h3>
    <p>This product contains nicotine, a chemical known to the State of California to cause birth defects or other reproductive harm. This product is for adult use only. Keep away from children and pets. Do not ingest or apply to the skin. If nicotine poisoning occurs seek immediate medical attention.</p>
    <h3>USE WITH CAUTION:</h3>
    <p>Lorem ipsum dolor sit amet, consectetur adipisicing elit, sed do eiusmod tempor incididunt ut labore et dolore magna aliqua. Ut enim ad minim veniam, quis nostrud exercitation ullamco</p>
  </div>
  <div class="icons">
    <svg width="18" height="18" viewBox="0 0 18 18"><circle cx="9" cy="9" r="7" fill="#fff"/></svg>
    <svg width="22" height="20" viewBox="0 0 22 20"><path d="M11 1 L21 19 H1 Z" fill="#fff" stroke="#fff" stroke-linejoin="round" stroke-width="2"/><rect x="10" y="7" width="2" height="6" fill="#111417"/><rect x="10" y="15" width="2" height="2" fill="#111417"/></svg>
    <svg width="18" height="20" viewBox="0 0 18 20" fill="none" stroke="#fff" stroke-width="1.5"><circle cx="10" cy="3" r="2"/><path d="M10 6 L8 12 L5 19 M8 12 L11 19 M9 8 L14 11"/><rect x="1" y="14" width="4" height="5"/></svg>
  </div>
  <div class="maker">MANUFACTURED BY:</div>
  <div class="origin">MADE IN<br>NEW ZEALAND</div>
  <div class="spec spec--volume">60ML</div>
  <div class="spec spec--strength">6MG</div>
</article>

<article class="label label--cinnamon">
  <div class="smoke" role="img" aria-label="Orange smoke wisps illustration"></div>
  <div class="range-band">PREMEMUM E-LIQUID</div>
  <h2 class="flavour">Cinnamon Blueberry<br>Muffin</h2>
  <div class="info">
    <h3>INGREDIENTS:</h3>
    <p class="caps">Vegetable glycerin, propylene glycol<br>Natural &amp; artificial flavor 3%<br>Nicotine by volume</p>
    <p>May contain trace elements of nuts or seeds</p>
    <h3>WARNING:</h3>
    <p>This product contains nicotine, a chemical known to the State of California to cause birth defects or other reproductive harm. This product is for adult use only. Keep away from children and pets. Do not ingest or apply to the skin. If nicotine poisoning occurs seek immediate medical attention.</p>
    <h3>USE WITH CAUTION:</h3>
    <p>Lorem ipsum dolor sit amet, consectetur adipisicing elit, sed do eiusmod tempor incididunt ut labore et dolore magna aliqua. Ut enim ad minim veniam, quis nostrud exercitation ullamco</p>
  </div>
  <div class="icons">
    <svg width="18" height="18" viewBox="0 0 18 18"><circle cx="9" cy="9" r="7" fill="#fff"/></svg>
    <svg width="22" height="20" viewBox="0 0 22 20"><path d="M11 1 L21 19 H1 Z" fill="#fff" stroke="#fff" stroke-linejoin="round" stroke-width="2"/><rect x="10" y="7" width="2" height="6" fill="#111417"/><rect x="10" y="15" width="2" height="2" fill="#111417"/></svg>
    <svg width="18" height="20" viewBox="0 0 18 20" fill="none" stroke="#fff" stroke-width="1.5"><circle cx="10" cy="3" r="2"/><path d="M10 6 L8 12 L5 19 M8 12 L11 19 M9 8 L14 11"/><rect x="1" y="14" width="4" height="5"/></svg>
  </div>
  <div class="maker">MANUFACTURED BY:</div>
  <div class="origin">MADE IN<br>NEW ZEALAND</div>
  <div class="spec spec--volume">60ML</div>
  <div class="spec spec--strength">6MG</div>
</article>

</body>
</html>
```